BRISKEL , FOLD LANTERN APA

Hey,

I would like to get a beer label that looks like Pemberly Guitar combo with master volume knob to show% ABV beer, beer Gain knob to show the style of APA and the Clean button to display the Best Data before. logo tag on the top of the briskel, under the middle part of Fold Lantern. lable overall dimensions are 162 millimeters wide and 90 millimeters high, the image should fit within the central part of the label area of ​​90x90 millimeters.
Attached files are easy to see my idea of label drawing , also can see my last beer label design (designed by Dale Wruton by my sketch)- a similar style I would like for the new label too.
Feel free to also create yours vision of this idea, it does not have to be exactly like my sketch. Briskel logo letters could be as in the wayward IPA label. The text could be a font of Antenna Black

Target Market(s)

craft beer drinkers, bars, pubs, beer shops etc

```html
<!DOCTYPE html>
<html lang="en">
<head>
<meta charset="utf-8">
<title>Briskel – Fold Lantern APA label</title>
<link rel="stylesheet" href="https://fonts.googleapis.com/css2?family=Montserrat:wght@700;800;900&family=Nunito:wght@800;900&display=swap">
<style>
  :root {
    --page: #ffffff;
    --amp-body: #262626;
    --amp-panel: #2b2b2b;
    --amp-dark: #1c1c1c;
    --logo-band: #000000;
    --grille-light: #2f2f2f;
    --grille-deep: #252525;
    --teal: #4bb3a6;
    --cream: #fdd47a;
    --red: #e83a2e;
    --ink: #1a1a1a;
    --white: #ffffff;
  }
  html, body {
    margin: 0;
    padding: 0;
    width: 1200px;
    height: 1000px;
    overflow: hidden;
    background: var(--page);
  }
  .label {
    display: block;
    width: 1200px;
    height: 1000px;
  }
  .tagline {
    font-family: "Nunito", sans-serif;
    font-weight: 900;
    font-size: 24px;
    fill: var(--cream);
  }
  .brand-name {
    font-family: "Montserrat", sans-serif;
    font-weight: 800;
    font-size: 128px;
    fill: var(--teal);
  }
  .beer-name {
    font-family: "Montserrat", sans-serif;
    font-weight: 900;
    font-size: 88px;
    fill: var(--cream);
    stroke: var(--ink);
    stroke-width: 12px;
    stroke-linejoin: round;
    paint-order: stroke fill;
  }
  .knob-text {
    font-family: "Montserrat", sans-serif;
    font-weight: 800;
    font-size: 22px;
    fill: var(--ink);
  }
  .brewed-text {
    font-family: "Montserrat", sans-serif;
    font-weight: 800;
    font-size: 22px;
    fill: var(--cream);
  }
</style>
</head>
<body>
<svg class="label" viewBox="0 0 1200 1000" xmlns="http://www.w3.org/2000/svg">
  <defs>
    <linearGradient id="grille-tone" x1="0" y1="0" x2="0" y2="1">
      <stop offset="0" stop-color="var(--grille-light)"/>
      <stop offset="1" stop-color="var(--grille-deep)"/>
    </linearGradient>
  </defs>

  <!-- amp cabinet -->
  <rect class="cabinet" x="135" y="35" width="927" height="927" fill="var(--amp-body)"/>

  <!-- top control strip -->
  <rect class="top-panel" x="250" y="42" width="698" height="113" fill="var(--amp-panel)"/>
  <rect class="top-stripe" x="256" y="58" width="687" height="22" fill="var(--red)"/>
  <text class="tagline" x="599" y="137" text-anchor="middle">Handcrafted unfiltered hopy beer for beerbrothers</text>

  <!-- corner handles and screws -->
  <path class="corner-cap" d="M172 62 q30 -6 60 -4 v20 h-50 q-10 -8 -10 -16z" fill="var(--cream)"/>
  <path class="corner-cap" d="M965 58 q32 -2 60 4 q0 8 -10 16 h-50z" fill="var(--cream)"/>
  <rect class="side-tick" x="163" y="100" width="7" height="48" fill="var(--cream)"/>
  <rect class="side-tick" x="1028" y="100" width="7" height="48" fill="var(--cream)"/>
  <rect class="side-tick" x="163" y="858" width="7" height="48" fill="var(--cream)"/>
  <rect class="side-tick" x="1028" y="858" width="7" height="48" fill="var(--cream)"/>
  <circle class="screw" cx="212" cy="134" r="9" fill="none" stroke="var(--cream)" stroke-width="6"/>
  <circle class="screw" cx="986" cy="134" r="9" fill="none" stroke="var(--cream)" stroke-width="6"/>
  <circle class="screw" cx="228" cy="873" r="9" fill="none" stroke="var(--cream)" stroke-width="6"/>
  <circle class="screw" cx="968" cy="873" r="9" fill="none" stroke="var(--cream)" stroke-width="6"/>

  <!-- side rails -->
  <rect class="side-rail" x="155" y="155" width="93" height="700" fill="var(--amp-panel)"/>
  <rect class="side-rail" x="958" y="155" width="87" height="700" fill="var(--amp-panel)"/>
  <rect class="rail-stripe" x="163" y="165" width="8" height="675" fill="var(--red)"/>
  <rect class="rail-stripe" x="1027" y="165" width="8" height="675" fill="var(--red)"/>

  <!-- brand band -->
  <rect class="logo-band" x="250" y="155" width="698" height="140" fill="var(--logo-band)"/>
  <text class="brand-name" x="599" y="272" text-anchor="middle" textLength="610" lengthAdjust="spacingAndGlyphs">BRISKEL</text>

  <!-- speaker grille area -->
  <rect class="grille" x="250" y="295" width="698" height="560" fill="url(#grille-tone)" role="img" aria-label="Amplifier speaker grille cloth texture"/>

  <!-- beer name speaker -->
  <circle class="speaker-rim" cx="597" cy="573" r="234" fill="var(--amp-dark)"/>
  <circle class="speaker-cone" cx="597" cy="573" r="225" fill="var(--teal)"/>
  <text class="beer-name" x="597" y="518" text-anchor="middle">FOLD</text>
  <text class="beer-name" x="597" y="610" text-anchor="middle" textLength="380" lengthAdjust="spacingAndGlyphs">LANTERN</text>
  <text class="beer-name" x="597" y="702" text-anchor="middle">APA</text>

  <!-- volume knob: ABV -->
  <circle class="knob-ring" cx="342" cy="766" r="62" fill="var(--amp-dark)"/>
  <circle class="knob" cx="342" cy="766" r="54" fill="var(--cream)"/>
  <line class="knob-pointer" x1="345" y1="756" x2="370" y2="731" stroke="var(--ink)" stroke-width="7" stroke-linecap="round"/>
  <text class="knob-text" x="340" y="785" text-anchor="middle">6.5%</text>
  <text class="knob-text" x="340" y="810" text-anchor="middle">ABV</text>

  <!-- gain knob: IBU -->
  <circle class="knob-ring" cx="860" cy="766" r="62" fill="var(--amp-dark)"/>
  <circle class="knob" cx="860" cy="766" r="54" fill="var(--cream)"/>
  <line class="knob-pointer" x1="832" y1="734" x2="856" y2="758" stroke="var(--ink)" stroke-width="7" stroke-linecap="round"/>
  <text class="knob-text" x="858" y="795" text-anchor="middle">50 IBU</text>

  <!-- bottom strip: brewed date -->
  <rect class="bottom-panel" x="250" y="858" width="698" height="72" fill="var(--amp-panel)"/>
  <rect class="brewed-tag" x="415" y="872" width="362" height="40" fill="var(--red)"/>
  <text class="brewed-text" x="430" y="900">BREWED</text>
  <rect class="brewed-field" x="555" y="882" width="207" height="20" fill="var(--white)"/>
</svg>
</body>
</html>
```